Postcard Design

Need postcard design for dental office. The doctor is returning to the office after a few months medical leave and he wants a postcard to be mailed to patients and families in the surrounding area to create new patients. We have attached a rough sketch of the information we would like to include on the postcard along with color selection but are open to additional artwork or design to improve the overall look. We are also including a photo of the dentist for the front of the postcard. We plan to have the metered postage through Quellmark if possible so please let me know how that works because I'm assuming that will need to be included in the design. I am also attaching a sample of a postcard that the dentist received in the mail from a Brindova doctor and would like his postcard to resemble this layout. The postcard needs to 8.5 x 5.5; I believe this is called the oversized selection for Quellmark and we are planning to have them do the printing. Please verify you did receive four attached files including photo, front sketch, back sketch, and actual postcard example.

Thank you,
Marisol Tepper

Medical

```html
<!DOCTYPE html>
<html lang="en">
<head>
<meta charset="utf-8">
<title>General Dentist Postcard</title>
<link rel="stylesheet" href="https://fonts.googleapis.com/css2?family=Marcellus&family=Source+Sans+3:wght@400&display=swap">
<style>
  :root {
    --bg: #ecebe8;
    --card-front: #f3f3f3;
    --card-white: #ffffff;
    --panel-grey: #f2f2f2;
    --green-dark: #0a6f36;
    --green-deep: #0c7a3b;
    --green-bright: #3bb54a;
    --lime: #8dc63f;
    --text-green: #0b6b33;
    --text-grey: #6d6e71;
    --text-dark: #555659;
    --white: #ffffff;
    --photo-top: #d9d9d8;
    --photo-mid: #8f8c89;
    --photo-low: #1f2226;
  }
  * { box-sizing: border-box; margin: 0; padding: 0; }
  html, body { width: 1015px; height: 1200px; overflow: hidden; }
  body { background: var(--bg); position: relative; font-family: "Marcellus", serif; }
  h2, p { font-weight: 400; }

  .postcard { position: absolute; width: 794px; height: 513px; overflow: hidden; }
  .postcard--front { left: 31px; top: 41px; background: var(--card-front); }
  .postcard--back { left: 165px; top: 622px; background: var(--card-white); }

  .green-band {
    position: absolute; left: 0; width: 100%;
    background: linear-gradient(90deg, var(--green-deep) 0%, var(--green-deep) 35%, var(--green-bright) 52%, var(--green-deep) 72%, var(--green-dark) 100%);
    color: var(--white);
  }
  .lime-stripe { position: absolute; left: 0; width: 100%; background: var(--lime); }

  /* Front */
  .dentist-photo {
    position: absolute; left: 0; top: 0; width: 297px; height: 423px;
    background: linear-gradient(180deg, var(--photo-top) 0%, var(--photo-top) 20%, var(--photo-mid) 45%, var(--photo-low) 70%, var(--photo-low) 100%);
  }
  .front-title {
    position: absolute; left: 638px; top: 30px; width: 150px;
    font-size: 28px; line-height: 34px; color: var(--text-grey); letter-spacing: 0.5px;
  }
  .front-headline {
    position: absolute; left: 297px; right: 0; top: 143px; text-align: center;
    font-size: 22px; color: var(--text-green); white-space: nowrap;
  }
  .front-doctor {
    position: absolute; left: 297px; right: 0; top: 224px; text-align: center;
    font-size: 20px; line-height: 30px; color: var(--text-green);
  }
  .front-doctor .phone { display: inline-flex; align-items: center; gap: 8px; }
  .front-doctor svg { width: 16px; height: 16px; fill: var(--text-green); }
  .office-address {
    position: absolute; left: 553px; width: 200px; top: 331px; text-align: center;
    font-family: "Source Sans 3", sans-serif; font-size: 16px; line-height: 21.5px; color: var(--text-dark);
    font-style: normal;
  }
  .postcard--front .green-band { top: 423px; height: 73px; }
  .postcard--front .lime-stripe { top: 496px; height: 4px; }
  .band-headline { position: absolute; left: 38px; top: 18px; font-size: 33px; letter-spacing: 0.3px; white-space: nowrap; }
  .band-info {
    position: absolute; left: 473px; top: 19px; width: 290px; text-align: center;
    font-family: "Source Sans 3", sans-serif; font-size: 14px; line-height: 19px; white-space: nowrap;
  }

  /* Back */
  .postcard--back .green-band { top: 0; height: 110px; }
  .postcard--back .lime-stripe { top: 110px; height: 18px; }
  .back-title { position: absolute; left: 38px; top: 28px; font-size: 30px; line-height: 36px; letter-spacing: 0.5px; }
  .back-offer {
    position: absolute; left: 262px; width: 510px; top: 33px; text-align: center;
    font-size: 22px; line-height: 29px; white-space: nowrap;
  }
  .bio-panel {
    position: absolute; left: 0; top: 128px; width: 395px; height: 385px;
    background: var(--panel-grey); padding: 38px 20px 0 37px;
    font-size: 19.5px; line-height: 31.5px; color: var(--text-grey);
  }
  .bio-panel p + p { margin-top: 16px; }
  .postage-box {
    position: absolute; left: 687px; top: 159px; width: 75px; height: 75px;
    border: 1.5px solid #c9c9c9; display: flex; align-items: center; justify-content: center; text-align: center;
    font-family: "Source Sans 3", sans-serif; font-size: 14px; line-height: 18.5px; color: var(--text-grey);
  }
</style>
</head>
<body>

<section class="postcard postcard--front">
  <div class="dentist-photo" role="img" aria-label="Portrait photograph of the dentist in a dark suit and tie"></div>
  <h2 class="front-title">GENERAL DENTIST</h2>
  <p class="front-headline">Now Accepting Established and New Patiens</p>
  <div class="front-doctor">
    <p>Leon R. Harwell, DDS, FAGD</p>
    <p class="phone">
      <svg viewBox="0 0 24 24" aria-hidden="true"><path d="M6.6 10.8a15.2 15.2 0 0 0 6.6 6.6l2.2-2.2a1 1 0 0 1 1-.25 11.4 11.4 0 0 0 3.6.57 1 1 0 0 1 1 1V20a1 1 0 0 1-1 1A17 17 0 0 1 3 4a1 1 0 0 1 1-1h3.5a1 1 0 0 1 1 1c0 1.250.2 2.45.57 3.57a1 1 0 0 1-.25 1z"/></svg>
      555-210-440
    </p>
  </div>
  <address class="office-address">
    Alder Springs<br>
    4820-B Fenwick Pkwy, Suite A<br>
    Alder Springs, GA 30199<br>
    555-210-4400
  </address>
  <div class="green-band">
    <p class="band-headline">NOW ACCEPTING PATIENS</p>
    <p class="band-info">For more information, please call<br>555 -210-4400 or visit DrLeonHarwell.com</p>
  </div>
  <div class="lime-stripe"></div>
</section>

<section class="postcard postcard--back">
  <div class="green-band">
    <h2 class="back-title">GENERAL<br>DENTIST</h2>
    <p class="back-offer">Accepting Established and New Patiens<br>call 555 -210-4400 or visit DrLeonHarwell.com</p>
  </div>
  <div class="lime-stripe"></div>
  <div class="bio-panel">
    <p>Leon R. Harwell DDS, FAGD, a native of Alder Springs, Ga earned his Doctorate of Dental Surgery at Ridgeview University Dental School in Halston.</p>
    <p>Dr. Harwell has been improving the dental health of patients in Western Georgia for over 25 years.</p>
  </div>
  <div class="postage-box">Stamp<br>metered<br>postage</div>
</section>

</body>
</html>
```